Cannabis Company needs a packaging design for a 4x6 pouch

We need a design for a new cannabis company. Included is the logo in red. The logo color can change. Whatever color looks best with the design is what we'll use. The design can't include any cartoon characters or anything that may appeal to children. We have multiple products that are similar that will be using the same design. The pouch will contain 10 pyramid shaped gummies. The look we're going for is modern, simple, but eye catching. I included a handful of photos of packaging we like if that helps.

```html
<!DOCTYPE html>
<html lang="en">
<head>
<meta charset="utf-8">
<title>Verdale Gummies Pouches</title>
<link rel="stylesheet" href="https://fonts.googleapis.com/css2?family=Josefin+Sans:wght@600;700&family=Sacramento&display=swap">
<style>
  :root {
    --canvas: #ffffff;
    --text-light: #ffffff;
    --apple-band-top: #0d4124;
    --apple-band-bottom: #05300f;
    --apple-accent: #8cc63f;
    --apple-bg-light: #f4f9ee;
    --apple-bg-mid: #c7e49a;
    --berry-band-top: #ec1b36;
    --berry-band-bottom: #d20a23;
    --berry-accent: #7a1020;
    --berry-bg-light: #fdf1f1;
    --berry-bg-mid: #f3a6a8;
  }
  * { margin: 0; padding: 0; box-sizing: border-box; }
  html, body { width: 1200px; height: 1200px; overflow: hidden; background: var(--canvas); }
  .stage { position: relative; width: 1200px; height: 1200px; }
  .pouch {
    position: absolute;
    top: 330px;
    width: 337px;
    height: 545px;
    overflow: hidden;
  }
  .pouch--apple { left: 194px; }
  .pouch--strawberry { left: 673px; }
  .pouch-art { position: absolute; inset: 0; }
  .pouch--apple .pouch-art {
    background: radial-gradient(circle at 20% 20%, var(--apple-bg-mid) 0%, transparent 35%),
                radial-gradient(circle at 70% 90%, var(--apple-bg-mid) 0%, transparent 35%),
                var(--apple-bg-light);
  }
  .pouch--strawberry .pouch-art {
    background: radial-gradient(circle at 20% 10%, var(--berry-bg-mid) 0%, transparent 30%),
                radial-gradient(circle at 45% 90%, var(--berry-bg-mid) 0%, transparent 35%),
                var(--berry-bg-light);
  }
  .label-band {
    position: absolute;
    inset: 0;
    clip-path: polygon(30px 136px, 309px 93px, 309px 414px, 30px 459px);
  }
  .pouch--apple .label-band { background: linear-gradient(160deg, var(--apple-band-top), var(--apple-band-bottom)); }
  .pouch--strawberry .label-band { background: linear-gradient(160deg, var(--berry-band-top), var(--berry-band-bottom)); }
  .label-content {
    position: absolute;
    left: 30px;
    width: 279px;
    top: 0;
    text-align: center;
    color: var(--text-light);
  }
  .brand-frame {
    position: absolute;
    left: 60px;
    top: 164px;
    width: 158px;
    height: 90px;
    border: 1px solid rgba(255,255,255,0.45);
    display: flex;
    align-items: center;
    justify-content: center;
  }
  .brand-name {
    font-family: "Josefin Sans", sans-serif;
    font-weight: 700;
    font-size: 30px;
    color: var(--text-light);
    line-height: 1;
  }
  .product-line {
    position: absolute;
    left: 0;
    width: 100%;
    font-family: "Josefin Sans", sans-serif;
    font-weight: 700;
    line-height: 1;
    letter-spacing: 1px;
  }
  .product-line--type { top: 274px; font-size: 26px; }
  .product-line--form { top: 302px; font-size: 36px; }
  .accent-rule {
    position: absolute;
    top: 345px;
    left: 111px;
    width: 57px;
    height: 2px;
  }
  .pouch--apple .accent-rule { background: var(--apple-accent); }
  .pouch--strawberry .accent-rule { background: var(--berry-accent); }
  .flavour {
    position: absolute;
    top: 352px;
    left: 0;
    width: 100%;
    font-family: "Sacramento", cursive;
    font-size: 36px;
    line-height: 34px;
  }
</style>
</head>
<body>
<main class="stage">
  <section class="pouch pouch--apple">
    <div class="pouch-art" role="img" aria-label="Green apples scattered over a light repeating leaf pattern"></div>
    <div class="label-band"></div>
    <div class="label-content">
      <div class="brand-frame"><span class="brand-name">Verdale</span></div>
      <p class="product-line product-line--type">DELTA 8 THC</p>
      <p class="product-line product-line--form">GUMMIES</p>
      <div class="accent-rule"></div>
      <p class="flavour">Apple<br>Flavour</p>
    </div>
  </section>

  <section class="pouch pouch--strawberry">
    <div class="pouch-art" role="img" aria-label="Ripe strawberries scattered over a light repeating leaf pattern"></div>
    <div class="label-band"></div>
    <div class="label-content">
      <div class="brand-frame"><span class="brand-name">Verdale</span></div>
      <p class="product-line product-line--type">DELTA 8 THC</p>
      <p class="product-line product-line--form">GUMMIES</p>
      <div class="accent-rule"></div>
      <p class="flavour">Strawberry<br>Flavour</p>
    </div>
  </section>
</main>
</body>
</html>
```